Website/Logo Design

We need a logo and website design for an opinion mining startup called VantroLux. Our technology mines the web to automatically discover what people are saying about brands, products, etc. The project we are fielding here is for our informational, public-facing website. In its initial incarnation, it will simply be a vehicle for marketing materials and information on our company and its offerings, but it should be flexible enough to expand as more content/functionality is added.

Some designs we like are:
http://www.brivel-nodo.com
http://www.tarnwisp.com
http://www.kvh.com
http://www.zellmorit.com
http://quontavel.com
http://marbiquex.com
http://www.vadup.com
Updates

All, please try to shy away from using a photo of a person as the focal point of the design.  Our company is more technological than social.

Target Market(s)

Primarily businesses interested in sentiment analysis (typically companies involved in advertising, market research, PR, etc.)

Industry/Entity Type

It Company

Requirements
Must have
• We are looking for a clean, modern, and professional design. This includes a logo, homepage, and internal page if it will differ from the homepage.
Nice to have
• It would be excellent if you could provide an HTML mockup if your design is chosen.
Should not have
• Flash, excessive bells and whistles

```html
<!DOCTYPE html>
<html lang="en">
<head>
<meta charset="utf-8">
<title>VantroLux</title>
<link href="https://fonts.googleapis.com/css2?family=Arimo:ital,wght@0,400;0,700;1,400&display=swap" rel="stylesheet">
<style>
:root{
  --bar:#000;
  --paper:#fff;
  --brand:#1b6690;
  --brand-dark:#1d5a82;
  --nav-muted:#9a9a9a;
  --text:#555;
  --rule:#c8c8c8;
  --quote-bg:#e3e3e3;
  --chirp:#4bbbe6;
}
*{margin:0;padding:0;box-sizing:border-box}
html,body{width:1200px;height:1197px;overflow:hidden;background:var(--paper)}
body{position:relative;font-family:"Arimo",Arial,sans-serif;color:var(--text)}
.top-bar,.bottom-bar{position:absolute;left:0;width:1200px;background:var(--bar)}
.top-bar{top:0;height:26px}
.bottom-bar{top:1135px;height:62px}

.main-nav{position:absolute;left:81px;top:104px;list-style:none}
.main-nav li{font-size:20px;line-height:37px;color:var(--nav-muted)}
.main-nav li.current{color:var(--brand)}

.wordmark{position:absolute;left:245px;top:92px;width:712px;height:225px;display:flex;align-items:center;justify-content:center;
  font-weight:700;font-size:150px;letter-spacing:-4px;color:var(--brand-dark)}

.social{position:absolute;left:1026px;top:178px;display:flex;align-items:center;gap:6px;font-size:15px;font-weight:700;color:var(--chirp)}
.social .dot{width:14px;height:14px;border-radius:50%;background:var(--chirp)}

h2{font-weight:400;color:var(--brand);font-size:20px;position:absolute}

.news h2{left:76px;top:395px}
.news-item{position:absolute;left:76px;width:148px;font-size:12px;line-height:16px}
.news-item .date{color:var(--brand);margin-bottom:8px}

.rule{position:absolute;top:420px;width:1px;height:392px;background:var(--rule)}

.welcome h2{left:301px;top:395px}
.welcome .copy{position:absolute;left:301px;top:424px;width:306px;height:396px;overflow:hidden;font-size:12px;line-height:16px}
.welcome .copy p{margin-bottom:7px}
.feature-photo{position:absolute;left:631px;top:424px;width:260px;height:196px;
  background:radial-gradient(ellipse at 45% 55%,#8a6a4c 0%,#4a3a2e 35%,#c9c9c9 80%,#e6e6e6 100%)}
.brand-chart{position:absolute;left:640px;top:680px;width:250px;height:142px;
  background:linear-gradient(90deg,#eceff3,#dde3ea 50%,#eef0f3)}

.testimonials h2{left:937px;top:389px}
.quote{position:absolute;left:936px;top:422px;width:160px;height:116px;background:var(--quote-bg);padding:9px 8px;
  font-size:10px;line-height:12px;font-style:italic;text-align:center;color:#666}
.quote::after{content:"";position:absolute;left:51px;bottom:-15px;border-left:9px solid transparent;border-right:9px solid transparent;border-top:15px solid var(--quote-bg)}
.testimonials h3{position:absolute;left:940px;top:565px;font-weight:400;font-size:16px;color:var(--brand)}
.testimonials .body{position:absolute;left:939px;top:584px;width:164px;font-size:10px;line-height:12px;color:#555}
.testimonials .body p{margin-bottom:10px}

.votes h2{left:159px;top:873px}
.vote-shot{position:absolute;top:912px;width:268px;height:158px;box-shadow:0 2px 5px rgba(0,0,0,.35)}
.vote-shot.one{left:159px;background:linear-gradient(180deg,#f6f8fa 0%,#e9f0f5 70%,#2e8fb5 78%,#2e8fb5 92%,#f6f8fa 100%)}
.vote-shot.two{left:455px;background:linear-gradient(90deg,#6e6a66 0%,#b7a99a 28%,#f1f1f1 30%,#e4e8ec 70%,#6f99c4 100%)}
.vote-shot.three{left:749px;background:linear-gradient(180deg,#1c1c1c 0%,#1c1c1c 25%,#8a2a18 45%,#c8892a 70%,#2a2a2a 100%)}
</style>
</head>
<body>
<div class="top-bar"></div>

<ul class="main-nav">
  <li class="current">home</li>
  <li>about</li>
  <li>rss</li>
  <li>submit</li>
  <li>contact us</li>
</ul>

<div class="wordmark">VantroLux</div>

<div class="social"><span class="dot"></span>Chirpwell</div>

<section class="news">
  <h2>latest news</h2>
  <div class="news-item" style="top:448px"><div class="date">28 May 2010</div>molore conse et, sit adipism odolum eu facil dolobore commy nulla vel inci blam dolorerat nonse dipisciduisi</div>
  <div class="news-item" style="top:581px"><div class="date">28 May 2010</div>molore conse et, sit adipism odolum eu facil dolobore commy nulla vel inci blam dolorerat nonse dipisciduis</div>
  <div class="news-item" style="top:714px"><div class="date">28 May 2010</div>molore conse et, sit adipism odolum eu facil dolobore commy nulla faccum alis alisciliquam in vel inci blam dolorerat nonse dipisciduis</div>
</section>

<div class="rule" style="left:257px"></div>

<section class="welcome">
  <h2>welcome to VantroLux</h2>
  <div class="copy">
    <p>molore conse et, sit adipism odolum eu facil dolobore commy nulla faccum alis alisciliquam in vel inci blam dolorerat nonse dipisciduisi blamcore cor irit am inibh et velent at. Agnibh eu facipis amcore min veniatue com-molore et in henim nim quate ex eumsa</p>
    <p>Dolut prat il dolore molore conse et, sit adipism odolum eu facil dolobore commy nulla faccum alis alisciliquam in vel inci blam dolorerat nonse dipisciduisi blamcore cor irit am inibh et velent at. Agnibh eu facipis amcore min veniatue commolore et in henim nim quate ex eumsa-molore conse et, sit adipism odolum eu facil dolobore commy nulla faccum alis alisciliquam in vel inci blam dolorerat nonse dipisciduisi blamcore cor irit am inibh et velent at. Agnibh eu facipis amcore min veniatue com-molore et in henim nim quate ex eumsa</p>
    <p>Dolut prat il dolore molore conse et, sit adipism odolum eu facil dolobore commy nulla faccum alis alisciliquam in vel inci blam dolorerat nonse dipisciduisi blamcore cor irit am inibh et velent at. Agnibh eu facipis amcore min veniatue commolore et in henim nim quate ex eumsa-molore conse et, sit adipism odolum eu facil dolobore commy nulla faccum alis alisciliquam in vel inci blam dolorerat nonse dipisciduisi blamcore cor irit am inibh et velent at. Agnibh eu facipis amcore min veniatue com-</p>
  </div>
  <div class="feature-photo" role="img" aria-label="Studio photo of carved wooden brand symbols on a grey backdrop"></div>
  <div class="brand-chart" role="img" aria-label="Infographic of brand preferences split by women 34% and men 66%"></div>
</section>

<div class="rule" style="left:913px"></div>

<section class="testimonials">
  <h2>testimonials</h2>
  <div class="quote">Dolut prat il dolore molore conse et, sit adipism odolum eu facil dolobore commy nulla faccum alis alisciliquam in vel inci blam dolorerat nonse dipisciduisi blamcore cor irit am inibh et velent at.<br>Agnibh eu facipis amcore min</div>
  <h3>Dolut prat il dolore</h3>
  <div class="body">
    <p>molore conse et, sit adipism odolum eu facil dolobore commy nulla faccum alis alisciliquam in vel inci blam dolorerat nonse dipisciduisi blamcore cor irit am inibh et velent at.<br>Agnibh eu facipis amcore min veniatue commolore et in henim nim quate ex eumsa</p>
    <p>Dolut prat il dolore molore conse et, sit adipism odolum eu facil dolobore commy nulla faccum alis alisciliquam in vel inci blam dolorerat nonse dipisciduisi blamcore cor irit am inibh et velent at.<br>Agnibh eu facipis amcore min veniatue commolore et in henim nim quate ex eumsa</p>
  </div>
</section>

<section class="votes">
  <h2>public votes</h2>
  <div class="vote-shot one" role="img" aria-label="Screenshot of a design marketplace homepage"></div>
  <div class="vote-shot two" role="img" aria-label="Screenshot of a newspaper website homepage"></div>
  <div class="vote-shot three" role="img" aria-label="Screenshot of a comic-style campaign website"></div>
</section>

<div class="bottom-bar"></div>
</body>
</html>
```